Kneadwell Haven Business Card Design

I want to create a very elegant and sophisticated two sided business card for my massage practice (www.kneadwellhaven-example.com). I have attached the logo and a PDF with some ideas down for the back of the card but I am open to suggestions. I will want to tie in a post card and flyer to the card later.
Similar colors to website would be great.
Target Market(s)
High end clientele, people looking for a sophisticated spa experience.
Industry/Entity Type
Massage
Contact Information for Business Card
Kneadwell Haven
7218 Larchmont Blvd S, Suite 305
Cedarvale, WA 98765
(555) 340-7816
www.kneadwellhaven-example.com

```html
<!DOCTYPE html>
<html lang="en">
<head>
<meta charset="utf-8">
<title>Kneadwell Haven – Business Card</title>
<link rel="stylesheet" href="https://fonts.googleapis.com/css2?family=EB+Garamond:wght@600;700&family=Open+Sans:wght@400&display=swap">
<style>
  :root {
    --backdrop: #1c1c1e;
    --card-navy: #1f3747;
    --card-white: #ffffff;
    --ink-light: #f1ede6;
    --ornament: #d9cbb6;
    --ink-dark: #1f3747;
    --ink-text: #3a3f45;
    --rule: #5d6872;
  }
  * { margin: 0; padding: 0; box-sizing: border-box; }
  html, body { width: 1200px; height: 960px; overflow: hidden; background: var(--backdrop); }
  .stage { position: relative; width: 1200px; height: 960px; }

  .card {
    position: absolute;
    width: 600px;
    height: 340px;
    box-shadow: 0 18px 40px rgba(0,0,0,.55);
  }

  /* Front side */
  .card--front {
    left: 120px; top: 80px;
    background: var(--card-navy);
    color: var(--ink-light);
    font-family: "EB Garamond", Georgia, serif;
    font-weight: 700;
    text-align: center;
  }
  .front__invite {
    position: absolute; left: 0; right: 0; top: 42px;
    font-size: 25px; line-height: 1.18;
    white-space: nowrap;
  }
  .front__ornament {
    position: absolute; left: 205px; top: 170px;
    width: 190px; height: 44px;
    background: var(--ornament);
    border-radius: 22px;
    opacity: .85;
  }
  .front__service {
    position: absolute; left: 0; right: 0; bottom: 36px;
    font-size: 22px;
    white-space: nowrap;
  }

  /* Back side */
  .card--back {
    left: 480px; top: 460px;
    background: var(--card-white);
    font-family: "Open Sans", Arial, sans-serif;
    color: var(--ink-text);
  }
  .back__brand {
    position: absolute; left: 30px; top: 0; bottom: 0; width: 250px;
    display: flex; align-items: center; justify-content: center;
    font-family: "EB Garamond", Georgia, serif;
    font-weight: 600;
    font-size: 31px;
    letter-spacing: 1px;
    text-transform: uppercase;
    color: var(--ink-dark);
    text-align: center;
    line-height: 1.1;
  }
  .back__divider {
    position: absolute; left: 300px; top: 66px;
    width: 1px; height: 208px; background: var(--rule);
  }
  .back__contact {
    position: absolute; left: 320px; top: 86px;
    font-size: 14px; line-height: 1.4;
    white-space: nowrap;
  }
  .contact__address { margin-bottom: 22px; }
  .contact__line { display: flex; align-items: center; gap: 8px; }
  .contact__line svg { width: 13px; height: 13px; flex: none; fill: var(--ink-dark); }
</style>
</head>
<body>
<main class="stage">
  <section class="card card--front" aria-label="Card front">
    <p class="front__invite">Step Inside and Discover the Most<br>Calming and Gently Restoring<br>Hour of Your Week.....</p>
    <div class="front__ornament" role="img" aria-label="Cream scrollwork flourish ornament"></div>
    <p class="front__service">Slow Tide Signature Calm Massage</p>
  </section>

  <section class="card card--back" aria-label="Card back">
    <div class="back__brand">Kneadwell<br>Haven</div>
    <div class="back__divider"></div>
    <div class="back__contact">
      <p class="contact__address">7218 Larchmont Blvd S, Suite 305<br>Cedarvale, WA 98765</p>
      <p class="contact__line">
        <svg viewBox="0 0 16 16" aria-hidden="true"><path d="M3.6 1.2l2.3 2.9-1.3 1.6c.9 2 2.6 3.7 4.6 4.6l1.6-1.3 2.9 2.3-1.4 2.4C6.5 13.4 2.6 9.5 1.2 3z"/></svg>
        (555) 340-7816
      </p>
      <p class="contact__line">
        <svg viewBox="0 0 16 16" aria-hidden="true"><path d="M1 3h14v10H1z M1.8 3.6L8 8.6l6.2-5" fill="none" stroke="#1f3747" stroke-width="1.4"/><path d="M1 3h14L8 8.6z"/></svg>
        ren@kneadwellhaven-example.com
      </p>
      <p class="contact__line">
        <svg viewBox="0 0 16 16" aria-hidden="true"><g fill="none" stroke="#1f3747" stroke-width="1.2"><circle cx="8" cy="8" r="6.5"/><ellipse cx="8" cy="8" rx="2.8" ry="6.5"/><path d="M1.5 8h13M2.6 4.6h10.8M2.6 11.4h10.8"/></g></svg>
        www.kneadwellhaven-example.com
      </p>
    </div>
  </section>
</main>
</body>
</html>
```